Vielen Dank für die tolle, schnelle Zusammenarbeit und den sympathischen Austausch!
Zielgruppe
Die Energie steckt in Dir!
Wer kennt ihn nicht diesen Punkt, an dem man merkt, es passt nicht mehr, die innerliche Freude, unsere kieselweg für das berufliche Tun ist weg. Es muss sich etwas ändern, doch wir wissen nicht wie. Verschiedene Dinge haben wir bereits ausprobiert, doch wir kommen nicht weiter.
Gut, wenn man einen unabhängigen und verschwiegenen Sparringspartner hat, bei dem man, das was einen beschäftigt, frei äußern darf, sein Gedanken-Karussell sortieren kann und der einen unterstützt, das eigene Ziel zu erreichen.
Die Energie steckt in Ihrem Unternehmen!
In der heutigen Zeit sind wir vielen internen und externen Einflüssen ausgesetzt (Digitalisierung, Änderung der Kundenwünsche, Führungswechsel, u.a.), die die Zusammenarbeit, Kommunikation und das Führungsverhalten im Unternehmen stark beeinflussen und die uns zwingen neue Wege zu gehen. Wollen wir weiterhin erfolgreich sein, müssen wir uns als Team an einen Tisch setzen und gemeinsam Planen, wie wir mit diesen Veränderungen umgehen und wie die Zukunft aussehen könnte.
Als Horizont-Lotsin begleite ich erfolgreiche Frauen (weibliche Fach- und Führungskräfte) und Teams in Veränderungsprozessen.
Ich lade sie ein, diesen Prozess AKTIV MITZUGESTALTEN, Ihr Umfeld einzubeziehen und KLAR und WERTSCHÄTZEND zu KOMMUNIZIEREN. Für mehr innere Balance. Für MEHR KIESELWEG am beruflichen Tun.
Ich bin davon überzeugt, alles Wissen und Energie in uns Menschen vorhanden ist, um Ziele erfolgreich zu meistern. Ich helfe Menschen und Teams, dieses Wissen/Wünsche freizusetzen, sie zu kommunizieren und ins Tun zu kommen.
Mein Angebot: Impuls-Coaching, Impuls-Seminare, Impuls-Workshops (World Café) rund um die Themen Veränderung, Kommunikation und Führung. Meine Konzept sind individuell auf die Einzelperson/ Unternehmen zugeschnitten (tailor-made).
Aufgabenstellung
Neue Infos:
Bild im Logo: eher abstrakt Richtung Energiewirbel o.ä., kein Tier, Blume o.ä.
Das Logo soll meinen Namen enthalten. Wahlweise Die Horizont-Lotsin, Impulse-Seminare, - Workshops & -Coaching, Die Energie steckt in Dir!. Für andere Zusammenstellung/ Ideen bin ich offen.
Ich könnte mir gut vorstellen, dass auf der Rückseite der Visitenkarte in einer Art Lexikoneintrag der Begriff „Horizont-Lotsin“ erklärt wird (siehe Beispiel anbei). Meine aktuelle Visitenkarte – Elemente/ der Schriftzug können übernommen werden, müssen aber nicht. Gut hat mir bisher auch das Foto auf der Rückseite gefallen.
Als Trainerin arbeite ich viel mit Powerpoint, daher wäre es schön, wenn (Teile der) die Elemente des Logos/ Corporate Design so gestaltet sind, dass sie sich für den Master einer Powerpoint „eignen“ bzw. sich dort mit wenig Platzaufwand widerspiegeln.
Der Briefbogen wird zu 90% digital verwendet.Einbinden des BKQF-Logos. Ggf. offenes Word-Dokument, so dass ich selbst etwas verändern kann.
Das Design an sich soll authentisch, klar, auf den Punkt, aktiv/begeisternd/dynamisch, wertvoll sein.
Bildsprache Frauen, Freude, Energie, Wohlfühlen. Veränderung.
Als Farben frisches, sattes Orange, dunkles grau (siehe Visitenkarte anbei).
Schrift klare, ggf. schwungvolle Schrift, aber nicht verschnörkelt.

```html
<!DOCTYPE html>
<html lang="de">
<head>
<meta charset="utf-8">
<title>Mareike Solten – Die Horizont-Lotsin</title>
<link rel="stylesheet" href="https://fonts.googleapis.com/css2?family=Open+Sans:ital,wght@0,400;0,600;0,700;1,400&family=Kaushan+Script&display=swap">
<style>
  :root {
    --orange: #e87a1c;
    --orange-light: #f29330;
    --orange-dark: #d9621f;
    --grey-dark: #4a4a4a;
    --grey-text: #555;
    --stage: #dfe3e8;
    --white: #ffffff;
  }
  * { margin: 0; padding: 0; box-sizing: border-box; }
  html, body { width: 1200px; height: 2253px; overflow: hidden; }
  body {
    position: relative;
    background: var(--stage);
    font-family: "Open Sans", Arial, sans-serif;
    color: var(--grey-text);
  }
  .brand-sheet {
    position: absolute; left: 0; top: 0;
    width: 1200px; height: 675px;
    background: var(--white);
  }
  .wordmark { position: absolute; left: 0; width: 100%; text-align: center; }
  .wordmark__dot {
    display: block; margin: 0 auto;
    border-radius: 50%;
    background: var(--orange);
  }
  .wordmark__name {
    display: block;
    color: var(--orange);
    font-weight: 400;
    letter-spacing: 0.02em;
  }
  .wordmark__tagline {
    display: block;
    color: var(--grey-dark);
    font-weight: 400;
    text-transform: uppercase;
    letter-spacing: 0.12em;
    line-height: 1.3;
  }
  .wordmark--hero { top: 162px; }
  .wordmark--hero .wordmark__dot { width: 140px; height: 140px; }
  .wordmark--hero .wordmark__name { font-size: 84px; line-height: 1; margin-top: 128px; }
  .wordmark--hero .wordmark__tagline { font-size: 27px; margin-top: 8px; }

  .card {
    position: absolute; left: 81px; width: 1041px; height: 332px;
    background: var(--white);
    box-shadow: 8px 8px 6px rgba(0,0,0,0.28);
    overflow: hidden;
  }
  .card--front { top: 778px; }
  .card--back { top: 1138px; }

  .card__slogan-panel {
    position: absolute; left: 0; top: 0; width: 519px; height: 100%;
    background: linear-gradient(90deg, var(--orange-light), var(--orange-dark));
    display: flex; align-items: center; justify-content: center;
  }
  .card__slogan {
    font-family: "Kaushan Script", cursive;
    color: var(--white);
    font-size: 50px; line-height: 1.25; text-align: center;
    font-weight: 400;
  }
  .card--front .wordmark { left: 519px; width: 522px; top: 80px; }
  .card--front .wordmark__dot { width: 70px; height: 70px; }
  .card--front .wordmark__name { font-size: 50px; line-height: 1; margin-top: 33px; }
  .card--front .wordmark__tagline { font-size: 15.5px; margin-top: 8px; }

  .card__portrait {
    position: absolute; left: 0; top: 0; width: 215px; height: 100%;
    background: linear-gradient(160deg, #c9c9c9 0%, #8d8d8d 55%, #3c3c3c 100%);
  }
  .lexicon { position: absolute; left: 240px; top: 66px; width: 300px; }
  .lexicon__term {
    font-size: 19.5px; font-weight: 700; line-height: 1.25;
    color: var(--grey-dark);
  }
  .lexicon__grammar { font-size: 14px; font-style: italic; color: var(--grey-dark); margin-top: 2px; }
  .lexicon__definition { font-size: 12.6px; line-height: 24px; margin-top: 8px; color: var(--grey-text); }

  .card__divider {
    position: absolute; left: 624px; top: 0; width: 2px; height: 100%;
    background: var(--orange);
  }
  .services { position: absolute; left: 652px; top: 40px; width: 360px; }
  .services__title {
    font-size: 20.5px; font-weight: 600; line-height: 1.3; color: var(--grey-dark);
  }
  .contact-list { list-style: none; position: absolute; left: 606px; top: 112px; }
  .contact-list__item {
    display: flex; align-items: center; height: 70px;
  }
  .contact-list__icon {
    width: 36px; height: 36px; border-radius: 50%;
    background: var(--orange);
    display: flex; align-items: center; justify-content: center;
    flex: none;
  }
  .contact-list__text {
    margin-left: 10px; font-size: 15px; line-height: 1.4; color: var(--grey-text);
  }
</style>
</head>
<body>
  <section class="brand-sheet">
    <div class="wordmark wordmark--hero">
      <span class="wordmark__dot"></span>
      <span class="wordmark__name">Mareike Solten</span>
      <span class="wordmark__tagline">Die Horizont-Lotsin</span>
    </div>
  </section>

  <section class="card card--front">
    <div class="card__slogan-panel">
      <p class="card__slogan">Die Energie<br>steckt in Dir!</p>
    </div>
    <div class="wordmark">
      <span class="wordmark__dot"></span>
      <span class="wordmark__name">Mareike Solten</span>
      <span class="wordmark__tagline">Die Horizont-Lotsin</span>
    </div>
  </section>

  <section class="card card--back">
    <div class="card__portrait" role="img" aria-label="Schwarz-Weiß-Porträtfoto der Coachin"></div>
    <div class="lexicon">
      <p class="lexicon__term">Ho | ri | zont | - | Lot | sin</p>
      <p class="lexicon__grammar">(Singular), Substantiv (f) [die];</p>
      <p class="lexicon__definition">die einlädt Veränderungen aktiv mit-<br>zugestalten und eigene Bedürfnisse klar<br>und wertschätzend zu kommunizieren.<br>Für mehr Kieselweg am beruflichen<br>Tun. Zur Erreichung persönlicher Ziele.</p>
    </div>
    <div class="card__divider"></div>
    <div class="services">
      <p class="services__title">Impulse-Seminare,<br>-Workshops &amp; -Coaching</p>
    </div>
    <ul class="contact-list">
      <li class="contact-list__item">
        <span class="contact-list__icon">
          <svg width="20" height="20" viewBox="0 0 20 20" aria-hidden="true"><path d="M10 3 L18 10 H15.5 V17 H11.5 V12.5 H8.5 V17 H4.5 V10 H2 Z" fill="#fff"/></svg>
        </span>
        <span class="contact-list__text">Ahornweg 14<br>45127 Essen</span>
      </li>
      <li class="contact-list__item">
        <span class="contact-list__icon">
          <svg width="20" height="20" viewBox="0 0 20 20" aria-hidden="true"><rect x="6" y="2.5" width="8" height="15" rx="1.5" fill="none" stroke="#fff" stroke-width="1.8"/><circle cx="10" cy="14.8" r="0.9" fill="#fff"/></svg>
        </span>
        <span class="contact-list__text">0201 / 47 29 31 08<br>0176 / 418 20 77</span>
      </li>
      <li class="contact-list__item">
        <span class="contact-list__icon">
          <svg width="20" height="20" viewBox="0 0 20 20" aria-hidden="true"><g fill="none" stroke="#fff" stroke-width="1.5"><circle cx="10" cy="10" r="7"/><ellipse cx="10" cy="10" rx="3" ry="7"/><path d="M3 10 H17 M4.2 6.3 H15.8 M4.2 13.7 H15.8"/></g></svg>
        </span>
        <span class="contact-list__text">kieselweg@mareike-solten.de<br>www.mareike-solten.de</span>
      </li>
    </ul>
  </section>
</body>
</html>
```